Vro Klinieken website for a maxillofacial surgery clinic

It's a website for a clinic for maxillofacial surgery in WordPress . The website doesn't need to be complicated but has to look professional. It needs to be in Dutch so i can give the texts. Similar websites are www.tandartsenpraktijkvelmor.nl or www.tbospecialisten.nl. Pages would be sort of similar to https://hetcentrumvoorgezichtszorg.nl/ or https://wolderveenclinics.nl/. Those lasts are maxillofacial surgery clinic websites, but there are little more extensive.
I uploaded the logo. If this is not the proper quality i can upload the eps. Logo was made through printhive.

Target Market(s)

Patients who can find me and see information about the clinic

Industry/Entity Type

Healthcare

Coding

Coded - Design and coding required

Number of Pages Required

5+ page

Font styles to use
Other font styles liked:
• Something standard professional

Colors
0054AA
0677BA
7BADD7
CADEEF
E8F1F8

Requirements
Nice to have
• Something in line with the logo. I prefer a little dark like the darker logos but I'm not sure if that's professional. Logos zbpor and gvls are instances i'm registered to so they will have to be on the website too but small somewhere.

```html
<!DOCTYPE html>
<html lang="nl">
<head>
<meta charset="utf-8">
<title>Vro Klinieken – Kaakchirurgie</title>
<link href="https://fonts.googleapis.com/css2?family=Fira+Sans:wght@400;500;600;700&family=Open+Sans:wght@400;600;700&display=swap" rel="stylesheet">
<style>
:root{
  --navy:#16384f;
  --navy-deep:#0f2c40;
  --sky:#29a8e0;
  --sky-dark:#1e93c8;
  --page:#f5f5f5;
  --ink:#2f3b47;
  --muted:#8a929a;
  --white:#ffffff;
  --footer:#222629;
  --footer-line:#34393d;
  --star:#f26b3a;
}
*{box-sizing:border-box;margin:0;padding:0}
html,body{width:1200px;height:4641px;overflow:hidden}
body{background:var(--page);font-family:"Open Sans",sans-serif;color:var(--ink);position:relative}
.abs{position:absolute}
h1,h2,h3,h4,.heading{font-family:"Fira Sans",sans-serif}
.section-title{position:absolute;left:0;width:1200px;text-align:center;font-size:31px;font-weight:500;color:var(--navy)}
.section-intro{position:absolute;left:0;width:1200px;text-align:center;font-size:13px;line-height:22px;color:var(--muted)}
.btn{position:absolute;display:flex;align-items:center;justify-content:center;background:var(--sky);color:var(--white);font-family:"Fira Sans",sans-serif;font-weight:600;font-size:14px;border-radius:4px}

/* header */
.topbar{top:0;left:0;width:1200px;height:29px;background:var(--white)}
.topbar-dark{top:0;left:400px;width:800px;height:29px;background:var(--navy-deep);clip-path:polygon(18px 0,100% 0,100% 100%,0 100%)}
.topbar-item{top:9px;font-size:10px;color:var(--white);font-weight:600}
.nav{top:29px;left:0;width:1200px;height:50px;background:var(--white)}
.logo{display:flex;align-items:center;gap:6px;font-family:"Fira Sans",sans-serif;font-weight:600;color:var(--sky);font-size:17px}
.logo-dot{width:18px;height:18px;border-radius:50%;background:var(--sky)}
.nav-link{top:49px;font-size:12px;color:var(--ink)}
.nav-link.active{font-weight:700;color:var(--navy)}

/* hero */
.hero{top:79px;left:0;width:1200px;height:633px;background:linear-gradient(100deg,#3c4a56 0%,#5d6e7b 35%,#8aa3b4 62%,#b7c9d4 100%)}
.hero-shade{top:79px;left:0;width:760px;height:633px;background:linear-gradient(90deg,rgba(22,40,55,.55),rgba(22,40,55,0))}
.hero-kicker{top:268px;left:110px;font-size:13px;color:var(--white);display:flex;align-items:center;gap:14px}
.hero-kicker span{display:inline-block;width:46px;height:1px;background:var(--white)}
.hero-title{top:322px;left:110px;font-size:44px;line-height:58px;color:var(--white);font-weight:600}
.hero-text{top:474px;left:110px;width:420px;font-size:13px;line-height:22px;color:var(--white)}

/* why cards */
.why-card{top:969px;width:234px;height:217px;background:var(--white);box-shadow:0 2px 10px rgba(0,0,0,.1);border-radius:4px;text-align:center;padding-top:32px}
.why-card.featured{background:var(--navy)}
.why-card svg{display:block;margin:0 auto 14px}
.why-card h3{font-size:18px;font-weight:500;line-height:25px;color:var(--navy)}
.why-card p{margin-top:8px;font-size:12.5px;line-height:22px;color:var(--muted);padding:0 24px}
.why-card.featured h3,.why-card.featured p{color:var(--white)}

/* about block */
.about-bg{top:1321px;left:281px;width:919px;height:468px;background:var(--navy)}
.about-photo{top:1387px;left:0;width:582px;height:445px;background:linear-gradient(135deg,#c9d6df,#6e9bb5 55%,#3a6f94)}
.about-title{top:1412px;left:633px;font-size:30px;color:var(--white);font-weight:500}
.about-text{left:631px;width:430px;font-size:12.5px;line-height:22px;color:var(--white)}

/* services */
.svc-photo{top:2063px;width:321px;height:234px}
.svc-box{top:2240px;width:284px;height:201px;background:var(--white);box-shadow:0 2px 10px rgba(0,0,0,.12);padding:26px 38px 0 38px}
.svc-box.featured{background:var(--navy)}
.svc-box h3{font-size:20px;font-weight:500;color:var(--navy)}
.svc-box p{margin-top:10px;font-size:12.5px;line-height:22px;color:var(--muted)}
.svc-box a{display:block;margin-top:10px;font-size:10.5px;font-weight:700;color:var(--sky);text-decoration:none}
.svc-box.featured h3,.svc-box.featured p,.svc-box.featured a{color:var(--white)}

/* cta */
.cta{top:2512px;left:0;width:1200px;height:295px;background:linear-gradient(90deg,#1f3446,#3b5164 50%,#26394a)}
.cta-phone{top:2560px;left:0;width:1200px;text-align:center;font-size:22px;color:var(--white);font-weight:500}
.cta-title{top:2600px;left:0;width:1200px;text-align:center;font-size:31px;color:var(--white);font-weight:600}
.cta-btn{top:2722px;left:519px;width:169px;height:44px;border:1.5px solid var(--white);border-radius:5px;display:flex;align-items:center;justify-content:center;color:var(--white);font-family:"Fira Sans",sans-serif;font-size:13px;font-weight:600}

/* testimonials */
.quote-card{top:3041px;width:494px;height:254px;background:#ebeef1}
.quote-line{top:45px;left:63px;width:1px;height:178px;background:#b7c2cb}
.quote-badge{top:110px;left:38px;width:50px;height:50px;border-radius:50%;background:var(--white);border:3px solid var(--sky);display:flex;align-items:center;justify-content:center;color:var(--sky);font-family:"Fira Sans",sans-serif;font-size:30px;font-weight:700;line-height:1}
.stars{top:38px;left:114px;color:var(--star);font-size:16px;letter-spacing:3px}
.quote-text{top:82px;left:114px;width:340px;font-size:12.5px;line-height:22px;color:var(--muted)}
.quote-name{top:180px;left:114px;font-size:17px;font-weight:600;color:var(--navy)}
.quote-place{top:205px;left:114px;font-size:11.5px;color:var(--muted)}
.quote-avatar{top:173px;left:399px;width:60px;height:60px;border-radius:50%;background:linear-gradient(135deg,#e8d6c6,#b7937a)}
.dot{top:3341px;width:10px;height:10px;border-radius:50%;background:var(--star)}
.dot.empty{background:transparent;border:1.5px solid var(--star)}

/* contact */
.contact-box{top:3595px;left:90px;width:1016px;height:463px;background:var(--white);box-shadow:0 2px 10px rgba(0,0,0,.08)}
.contact-side{top:3595px;left:90px;width:509px;height:463px;background:linear-gradient(135deg,#3c5d77,#1b3f5a 60%,#16384f)}
.contact-info{left:176px;color:var(--white);font-weight:700}
.field{left:688px;width:332px;height:33px;background:#f5f6f7;border:1px solid #eceef0;font-size:9.5px;color:var(--muted);padding:10px 14px}
.soc{top:3965px;width:31px;height:31px;border-radius:50%;background:rgba(255,255,255,.4)}

/* footer */
.footer{top:4189px;left:0;width:1200px;height:452px;background:var(--footer)}
.infobar{top:4139px;left:65px;width:1070px;height:104px;background:var(--sky);border-radius:6px}
.info-item{top:4166px;color:var(--white);display:flex;gap:18px;align-items:flex-start}
.info-item h4{font-size:18px;font-weight:500}
.info-item p{margin-top:10px;font-size:12px;font-weight:600}
.divider{top:4139px;width:2px;height:104px}
.foot-head{top:4314px;font-size:18px;font-weight:600;color:var(--white)}
.foot-text{font-size:12.5px;line-height:30px;color:var(--white)}
.foot-link{font-size:12.5px;color:var(--white);text-decoration:underline}
.subscribe{top:4488px;left:796px;width:340px;height:54px;background:var(--white);border-radius:3px;font-size:12px;color:var(--muted);padding:18px 16px}
.subscribe-btn{top:4488px;left:1073px;width:63px;height:54px;background:var(--sky);border-radius:0 3px 3px 0}
.bottombar{top:4577px;left:0;width:1200px;height:64px;border-top:1px solid var(--footer-line)}
.bottom-logo{top:4578px;left:65px;width:171px;height:63px;background:var(--sky);display:flex;align-items:center;justify-content:center}
.bottom-soc{top:4578px;width:56px;height:63px;border-left:1px solid var(--footer-line);display:flex;align-items:center;justify-content:center}
.bottom-soc span{width:12px;height:12px;border-radius:50%;background:#4b5054}
</style>
</head>
<body>

<!-- Header -->
<div class="abs topbar"></div>
<div class="abs topbar-dark"></div>
<div class="abs topbar-item" style="left:467px">● 48 Lindelaan, Velmor</div>
<div class="abs topbar-item" style="left:703px">VOLG ONS &nbsp;● ● ●</div>
<div class="abs topbar-item" style="left:856px">AFSPRAAK MAKEN</div>
<div class="abs nav"></div>
<div class="abs logo" style="top:42px;left:118px"><span class="logo-dot"></span>Vro Klinieken</div>
<div class="abs nav-link active" style="left:402px">Thuis</div>
<div class="abs nav-link" style="left:472px">Behandelingen</div>
<div class="abs nav-link" style="left:608px">Vergoeding</div>
<div class="abs nav-link" style="left:709px">Ons team</div>
<div class="abs nav-link" style="left:796px">Folders</div>
<div class="abs nav-link" style="left:865px">Contact Us</div>

<!-- Hero -->
<div class="abs hero" role="img" aria-label="Foto van een tandarts die een lachende patiënte behandelt"></div>
<div class="abs hero-shade"></div>
<div class="abs hero-kicker">On the other hand <span></span></div>
<h1 class="abs hero-title">Zelfvertrouwen Boetseren,<br>Levens Vormgeven</h1>
<p class="abs hero-text">Lorem ipsum dolor sit amet, consectetur adipiscing elit, sed d o eiusmod temp dipiscing elit, sed d</p>
<div class="btn" style="top:556px;left:110px;width:169px;height:47px;font-size:13px">Contact Us</div>

<!-- Why -->
<h2 class="section-title" style="top:840px">Waarom Voor Ons Kiezen</h2>
<p class="section-intro" style="top:894px">Lorem ipsum dolor sit amet, consectetur adipiscing elit, sed do eiusmod tempor<br>incididunt ut labore et dolore magna aliqua. Ut enim ad min</p>

<div class="abs why-card" style="left:92px">
  <svg width="38" height="38" viewBox="0 0 38 38" fill="none" stroke="#29a8e0" stroke-width="2"><polygon points="19,4 31,11 34,24 25,34 13,34 4,24 7,11"/><circle cx="19" cy="20" r="6"/></svg>
  <h3>Persoonlijke<br>Aanpak</h3><p>Lorem ipsum dolor sit amet, consectetur adipiscing</p>
</div>
<div class="abs why-card featured" style="left:352px">
  <svg width="38" height="38" viewBox="0 0 38 38" fill="none" stroke="#29a8e0" stroke-width="2"><path d="M8 32h22M12 32l4-10 8-14 5 3-8 14-9 7"/><circle cx="26" cy="24" r="3"/></svg>
  <h3>Bewezen<br>Track Record</h3><p>Lorem ipsum dolor sit amet, consectetur adipiscing</p>
</div>
<div class="abs why-card" style="left:612px">
  <svg width="38" height="38" viewBox="0 0 38 38" fill="none" stroke="#29a8e0" stroke-width="2"><path d="M6 26a13 13 0 1 1 26 0"/><rect x="5" y="24" width="6" height="9" rx="2"/><rect x="27" y="24" width="6" height="9" rx="2"/><path d="M19 16v8"/></svg>
  <h3>Kwalite-<br>itsborging</h3><p>Lorem ipsum dolor sit amet, consectetur adipiscing</p>
</div>
<div class="abs why-card" style="left:872px">
  <svg width="38" height="38" viewBox="0 0 38 38" fill="none" stroke="#29a8e0" stroke-width="2"><circle cx="19" cy="13" r="7"/><path d="M6 34c0-8 6-12 13-12s13 4 13 12z"/></svg>
  <h3 style="line-height:50px;margin-top:-12px">Klantgericht</h3><p style="margin-top:-4px">Lorem ipsum dolor sit amet, consectetur adipiscing</p>
</div>
<div class="btn" style="top:1223px;left:523px;width:167px;height:47px;font-size:13px">Meer Leren</div>

<!-- About -->
<div class="abs about-bg"></div>
<div class="abs about-photo" role="img" aria-label="Foto van het zorgteam met een patiënte in de behandelkamer"></div>
<h2 class="abs about-title">Gezichten Kracht Geven</h2>
<p class="abs about-text" style="top:1466px">Lorem ipsum dolor sit amet, consectetur adipiscing elit, sed do eiusmod tempor &nbsp;incididunt ut labore et dolore magna aliqua. Ut e nim ad min veniam, quis nostrud ex.</p>
<p class="abs about-text" style="top:1541px">Lorem ipsum dolor sit amet, consectetur adipiscing elit, sed do eiusmod tempor &nbsp;incididunt ut labore et dolore magna aliqua. Ut e nim ad min veniam, quis nostrud ex. et dolore magna aliqua. Ut e nim ad min veniam, quis nostrud ex.</p>
<div class="btn" style="top:1651px;left:631px;width:156px;height:45px;gap:12px">Meer Leren
  <svg width="18" height="14" viewBox="0 0 18 14" fill="none" stroke="#fff" stroke-width="2"><path d="M1 7h15M10 1l6 6-6 6"/></svg></div>

<!-- Services -->
<h2 class="section-title" style="top:1910px">Onze Diensten</h2>
<p class="section-intro" style="top:1964px">Lorem ipsum dolor sit amet, consectetur adipiscing elit, sed do eiusmod tempor<br>incididunt ut labore et dolore magna aliqua. Ut enim ad min</p>

<div class="abs svc-photo" style="left:92px;background:linear-gradient(135deg,#c7d5de,#6f95ad)" role="img" aria-label="Foto van een kaakchirurg die een oudere patiënt behandelt"></div>
<div class="abs svc-photo" style="left:440px;background:linear-gradient(135deg,#8fc7e2,#3f7fa6)" role="img" aria-label="Foto van een kind in de behandelstoel"></div>
<div class="abs svc-photo" style="left:786px;background:linear-gradient(135deg,#dfe5ea,#9ab4c6)" role="img" aria-label="Foto van een patiënte tijdens een controle"></div>

<div class="abs svc-box" style="left:112px"><h3>Kaakchirurgie</h3><p>Lorem ipsum dolor sit amet, cons ectetur adipiscing elit, sed do eiu smod tempor incididunt ut labore et dolore magna aliqua.</p><a>MEER LEREN</a></div>
<div class="abs svc-box featured" style="left:459px"><h3>Slaapgeneeskunde</h3><p>Lorem ipsum dolor sit amet, cons ectetur adipiscing elit, sed do eiu smod tempor incididunt ut labore et dolore magna aliqua.</p><a>MEER LEREN</a></div>
<div class="abs svc-box" style="left:805px"><h3>Plastische Chirurgie</h3><p>Lorem ipsum dolor sit amet, cons ectetur adipiscing elit, sed do eiu smod tempor incididunt ut labore et dolore magna aliqua.</p><a>MEER LEREN</a></div>

<!-- CTA -->
<div class="abs cta" role="img" aria-label="Gedimde foto van lachende zorgverleners en patiënten"></div>
<div class="abs cta-phone heading">123-456-7890</div>
<h2 class="abs cta-title">Ontvang vandaag gratis consultatie</h2>
<p class="section-intro" style="top:2657px;color:#e6ebef">Lorem ipsum dolor sit amet, consectetur adipiscing elit, sed do eiusmod tempor<br>incididunt ut labore et dolore magna aliqua. Ut enim ad min</p>
<div class="abs cta-btn">Contact Us</div>

<!-- Testimonials -->
<h2 class="section-title" style="top:2891px">Wat Klanten Zeggen</h2>
<p class="section-intro" style="top:2945px">Lorem ipsum dolor sit amet, consectetur adipiscing elit, sed do eiusmod tempor<br>incididunt ut labore et dolore magna aliqua. Ut enim ad min</p>

<div class="abs quote-card" style="left:90px">
  <div class="abs quote-line"></div><div class="abs quote-badge">“</div>
  <div class="abs stars">★★★★★</div>
  <p class="abs quote-text">Lorem ipsum dolor sit amet, consectetur adipiscing elit, sed do eiusmod tempor incididunt ut labore et d olore magna aliqua.</p>
  <div class="abs quote-name heading">Marloes de Wit</div><div class="abs quote-place">Zonnedal</div>
  <div class="abs quote-avatar" role="img" aria-label="Profielfoto van de klant"></div>
</div>
<div class="abs quote-card" style="left:609px">
  <div class="abs quote-line"></div><div class="abs quote-badge">“</div>
  <div class="abs stars">★★★★★</div>
  <p class="abs quote-text">Lorem ipsum dolor sit amet, consectetur adipiscing elit, sed do eiusmod tempor incididunt ut labore et d olore magna aliqua.</p>
  <div class="abs quote-name heading">Marloes de Wit</div><div class="abs quote-place">Zonnedal</div>
  <div class="abs quote-avatar" role="img" aria-label="Profielfoto van de klant"></div>
</div>
<div class="abs dot" style="left:565px"></div>
<div class="abs dot" style="left:584px"></div>
<div class="abs dot empty" style="left:602px"></div>
<div class="abs dot" style="left:620px"></div>

<!-- Contact -->
<h2 class="section-title" style="top:3446px">Kom Met Ons In Contact</h2>
<p class="section-intro" style="top:3500px">Lorem ipsum dolor sit amet, consectetur adipiscing elit, sed do eiusmod tempor<br>incididunt ut labore et dolore magna aliqua. Ut enim ad min</p>

<div class="abs contact-box"></div>
<div class="abs contact-side" role="img" aria-label="Gedimde foto van een medewerker aan de balie"></div>
<div class="abs contact-info" style="top:3662px;font-size:16px">CONTACT US</div>
<div class="abs contact-info heading" style="top:3699px;font-size:21px;font-weight:600">Call: 0123456789</div>
<div class="abs contact-info" style="top:3734px;font-size:11px">info@company.com</div>
<div class="abs contact-info" style="top:3782px;font-size:11px;line-height:17px">Address:<br>SOME PLACE<br>51100 Road</div>
<div class="abs contact-info" style="top:3856px;font-size:11px;line-height:17px">Operating Hours<br>Monday to Saturday: 9:00 - 18:00<br>Sunday: Closed</div>
<div class="abs soc" style="left:179px"></div>
<div class="abs soc" style="left:220px;background:var(--white)"></div>
<div class="abs soc" style="left:261px"></div>
<div class="abs soc" style="left:302px"></div>

<div class="abs heading" style="top:3653px;left:687px;font-size:17px;font-weight:600;color:var(--navy-deep)">FREE CONSULTATION</div>
<div class="abs field" style="top:3705px">Your Name</div>
<div class="abs field" style="top:3754px">Email</div>
<div class="abs field" style="top:3803px">Phone</div>
<div class="abs field" style="top:3854px;height:92px">Message</div>
<div class="btn" style="top:3965px;left:688px;width:110px;height:37px;font-size:11px">SUBMIT</div>

<!-- Footer -->
<div class="abs footer"></div>
<div class="abs infobar"></div>
<svg class="abs divider" style="left:405px;width:30px" viewBox="0 0 30 104" fill="none" stroke="#fff" stroke-width="2"><path d="M5 0l20 52-20 52"/></svg>
<svg class="abs divider" style="left:762px;width:30px" viewBox="0 0 30 104" fill="none" stroke="#fff" stroke-width="2"><path d="M5 0l20 52-20 52"/></svg>
<div class="abs info-item" style="left:106px">
  <svg width="54" height="50" viewBox="0 0 54 50" fill="none" stroke="#fff" stroke-width="2"><path d="M27 38s-11-12-11-20a11 11 0 0 1 22 0c0 8-11 20-11 20z"/><circle cx="27" cy="18" r="4"/><path d="M14 34L4 48h46L40 34"/></svg>
  <div><h4 class="heading">Locatie</h4><p>123, City, Country</p></div>
</div>
<div class="abs info-item" style="left:472px">
  <svg width="34" height="50" viewBox="0 0 34 50" fill="none" stroke="#fff" stroke-width="2"><rect x="5" y="3" width="24" height="44" rx="4"/><path d="M14 41h6"/></svg>
  <div><h4 class="heading">Telefoon</h4><p>+123 456 78890</p></div>
</div>
<div class="abs info-item" style="left:820px">
  <svg width="50" height="50" viewBox="0 0 50 50" fill="none" stroke="#fff" stroke-width="2"><rect x="4" y="14" width="42" height="30"/><path d="M4 14l21 16 21-16M4 44l15-13M46 44L31 31M12 14V4h26v10"/></svg>
  <div><h4 class="heading">Email</h4><p>info@company.com</p></div>
</div>

<div class="abs foot-head heading" style="left:67px">About Company</div>
<p class="abs foot-text" style="top:4379px;left:67px;width:320px">Lorem ipsum dolor sit amet, consectetur adipis cing elit, sed do eiusmod tempor incididunt ut labore et dolore magna aliqua.</p>
<div class="abs" style="top:4492px;left:67px;font-size:15px;color:var(--sky);text-decoration:underline">Read More</div>

<div class="abs foot-head heading" style="left:434px">Useful Links</div>
<div class="abs foot-link" style="top:4387px;left:434px">About Us</div>
<div class="abs foot-link" style="top:4420px;left:434px">Projects</div>
<div class="abs foot-link" style="top:4454px;left:434px">Blog</div>
<div class="abs foot-link" style="top:4488px;left:434px">Contact Us</div>
<div class="abs foot-link" style="top:4387px;left:610px">Services</div>
<div class="abs foot-link" style="top:4420px;left:610px">Shop</div>
<div class="abs foot-link" style="top:4454px;left:610px">Privacy Policy</div>
<div class="abs foot-link" style="top:4488px;left:610px">Help Desk</div>

<div class="abs foot-head heading" style="left:798px">Subscribe</div>
<p class="abs" style="top:4385px;left:797px;width:340px;font-size:13px;line-height:24px;color:var(--white);font-weight:600">If you have any questions, Subscribe to our newsleeter to know more</p>
<div class="abs subscribe">Email</div>
<div class="abs subscribe-btn"><svg width="63" height="54" viewBox="0 0 63 54" fill="none" stroke="#fff" stroke-width="2.5"><path d="M28 19l8 8-8 8"/></svg></div>

<div class="abs bottombar"></div>
<div class="abs bottom-logo"><div class="logo" style="color:var(--white)"><span class="logo-dot" style="background:var(--white)"></span>Vro Klinieken</div></div>
<div class="abs bottom-soc" style="left:902px"><span></span></div>
<div class="abs bottom-soc" style="left:958px"><span></span></div>
<div class="abs bottom-soc" style="left:1014px"><span></span></div>
<div class="abs bottom-soc" style="left:1070px"><span></span></div>
<div class="abs bottom-soc" style="left:1126px;width:74px"></div>

</body>
</html>
```